Business Card Design

Name of company: Brisk Property Maintenance.
We are a new start up business.
The company is involved in general property maintenance around residential properties and high rise apartment buildings.
We carry out all types of property maintenance such as:
*Handyman work
*Plumbing
*Painting
*Electrical
*Window cleaning
*Gardens / Landscaping

Target Market(s)

*Real Estate Agents
*Body corporate managers
*Private apartment owners

Industry/Entity Type

Property Maintenance

Requirements
Must have
• Name: Dean Malloy
Address: PO Box 3862
Carrow Hill Crossing
NSW 2746
Phone: 0431 962 305
Email: dean@briskpropertymaintenance
Website: www.briskpropertymaintenance.example.au
Nice to have
• We don't have any corporate logo so you can design what you think is appropriate

```html
<!DOCTYPE html>
<html lang="en">
<head>
<meta charset="utf-8">
<title>Brisk Property Maintenance – Business Card</title>
<link rel="stylesheet" href="https://fonts.googleapis.com/css2?family=Raleway:wght@300;800&display=swap">
<style>
  :root {
    --backdrop: #e6e6e4;
    --card-teal: #3dc0ca;
    --ink-white: #ffffff;
    --accent-red: #e8504f;
  }
  * { box-sizing: border-box; margin: 0; padding: 0; }
  html, body {
    width: 1200px;
    height: 899px;
    overflow: hidden;
    background: var(--backdrop);
  }
  .canvas {
    position: relative;
    width: 1200px;
    height: 899px;
  }
  .business-card {
    position: absolute;
    left: 100px;
    top: 164px;
    width: 1000px;
    height: 572px;
    background: var(--card-teal);
    color: var(--ink-white);
    font-family: "Raleway", sans-serif;
    box-shadow: 0 6px 18px rgba(0,0,0,0.15);
  }
  .brand {
    position: absolute;
    left: 60px;
    top: 56px;
    display: flex;
    align-items: center;
    gap: 26px;
  }
  .brand-name {
    font-weight: 800;
    font-size: 52px;
    letter-spacing: 0.5px;
    line-height: 1;
  }
  .brand-mark {
    width: 40px;
    height: 40px;
    background: var(--accent-red);
  }
  .divider-bar {
    position: absolute;
    left: 160px;
    top: 150px;
    width: 9px;
    height: 340px;
    background: var(--ink-white);
  }
  .contact-list {
    position: absolute;
    left: 200px;
    top: 150px;
    list-style: none;
  }
  .contact-line {
    display: flex;
    align-items: center;
    height: 44px;
    font-weight: 300;
    font-size: 33px;
    line-height: 1;
    letter-spacing: 0.3px;
    white-space: nowrap;
  }
  .contact-icon {
    width: 28px;
    height: 28px;
    margin-right: 26px;
    flex: none;
    fill: var(--accent-red);
  }
  .contact-icon.blank { fill: none; }
</style>
</head>
<body>
<div class="canvas">
  <section class="business-card">
    <div class="brand">
      <h1 class="brand-name">Brisk Property Maintenance</h1>
      <span class="brand-mark" aria-hidden="true"></span>
    </div>

    <div class="divider-bar" aria-hidden="true"></div>

    <ul class="contact-list">
      <li class="contact-line">
        <svg class="contact-icon" viewBox="0 0 24 24" aria-hidden="true"><circle cx="12" cy="7" r="5"/><path d="M3 23c0-6 4-9 9-9s9 3 9 9z"/></svg>
        Dean Malloy
      </li>
      <li class="contact-line">
        <svg class="contact-icon" viewBox="0 0 24 24" aria-hidden="true"><path d="M12 1a8 8 0 0 0-8 8c0 6 8 14 8 14s8-8 8-14a8 8 0 0 0-8-8zm0 11a3 3 0 1 1 0-6 3 3 0 0 1 0 6z"/></svg>
        PO Box 3862
      </li>
      <li class="contact-line">
        <svg class="contact-icon blank" viewBox="0 0 24 24" aria-hidden="true"></svg>
        Carrow Hill Crossing
      </li>
      <li class="contact-line">
        <svg class="contact-icon blank" viewBox="0 0 24 24" aria-hidden="true"></svg>
        NSW 2746
      </li>
      <li class="contact-line">
        <svg class="contact-icon" viewBox="0 0 24 24" aria-hidden="true"><path d="M6.6 10.8a15 15 0 0 0 6.6 6.6l2.2-2.2a1 1 0 0 1 1-.25 11 11 0 0 0 3.6.6 1 1 0 0 1 1 1V20a1 1 0 0 1-1 1A17 17 0 0 1 3 4a1 1 0 0 1 1-1h3.5a1 1 0 0 1 1 1 11 11 0 0 0 .6 3.6 1 1 0 0 1-.25 1z"/></svg>
        0431 962 305
      </li>
      <li class="contact-line">
        <svg class="contact-icon" viewBox="0 0 24 24" aria-hidden="true"><path d="M2 5h20v14H2z"/><path d="M3 6l9 7 9-7" fill="none" stroke="#3dc0ca" stroke-width="1.8"/></svg>
        dean@briskpropertymaintenance
      </li>
      <li class="contact-line">
        <svg class="contact-icon" viewBox="0 0 24 24" aria-hidden="true"><circle cx="12" cy="12" r="10"/><path d="M2 12h20M12 2c3 3 3 17 0 20M12 2c-3 3-3 17 0 20" fill="none" stroke="#3dc0ca" stroke-width="1.6"/></svg>
        www.briskpropertymaintenance.example.au
      </li>
    </ul>
  </section>
</div>
</body>
</html>
```